VELDAX

Our new site consists of: - Publish a regulatory watch by allowing access to the latest regulations and news specific to its field of activity. It will be asked when registering to choose 2 areas of activity from a predefined list - Make available the customs documents (DAU) and reverse charge reports - Establishment of a personal space project on which we bring our customs expertise to the client in order to change the management of its flows, this space will also allow him to keep his authorizations, RTC etc - Exhibit statistical tools (graph, curves ...) from the customs documents loaded on the site Our targets are our current customers, our prospects (importers, exporters) There will therefore be a personal secure access to create. The colors and tones must remain on the logo. "Logical" contrasts are appreciated.

Target Market(s)

importer / exporters

Font styles to use
Serif
Sans Serif

Colors

Designer to choose colors to be used in the design.

Requirements
Must have
• the following topics: - regulatory watch (modern newspaper template) - pdf file release (summary)
Nice to have
• a modern and functional design

```html
<!DOCTYPE html>
<html lang="en">
<head>
<meta charset="utf-8">
<title>VELDAX</title>
<link href="https://fonts.googleapis.com/css2?family=Lato:ital,wght@0,400;0,700;0,900;1,400&family=Open+Sans:wght@700;800&display=swap" rel="stylesheet">
<style>
:root{
  --orange:#ef4a24;
  --blue:#2a8fd6;
  --ink:#111;
  --text:#555;
  --muted:#999;
  --line:#d9d9d9;
  --soft:#f2f2f2;
  --footer:#000;
}
*{margin:0;padding:0;box-sizing:border-box}
html,body{width:1200px;height:3668px;overflow:hidden}
body{position:relative;background:#fff;font-family:'Lato',sans-serif;color:var(--ink)}
.abs{position:absolute}
.topline{left:0;top:0;width:1200px;height:4px;background:var(--blue)}
.logo{left:88px;top:26px;display:flex;align-items:center;gap:12px;font-weight:900;font-size:32px;line-height:1;color:var(--ink);letter-spacing:1px}
.logo i{width:16px;height:16px;background:var(--orange);display:block}
.nav{top:36px;font-size:17px;font-weight:700;color:#222}
.nav.active{color:var(--orange)}
.login{left:959px;top:24px;width:150px;height:44px;border-radius:22px;background:var(--orange);color:#fff;font-size:19px;display:flex;align-items:center;justify-content:center}
.hero{left:0;top:90px;width:1200px;height:539px;background:linear-gradient(90deg,#e9e4de 0%,#d8cfc3 35%,#b9a894 60%,#8c7d6c 100%)}
.hero-title{left:86px;top:236px;font-family:'Open Sans',sans-serif;font-weight:800;font-size:72px;line-height:1;color:var(--orange);letter-spacing:1px}
.hero-sub{left:88px;top:323px;font-size:20px;line-height:26px;color:var(--blue)}
.hero-btn{left:90px;top:414px;width:196px;height:56px;border:2px solid var(--orange);border-radius:28px;color:var(--orange);font-weight:900;font-size:16px;display:flex;align-items:center;justify-content:center}
.dot{top:578px;width:12px;height:12px;background:var(--orange)}
.dot.on{background:var(--blue)}
.post{left:90px;width:674px}
.post .cat{top:0;width:100%;text-align:center;font-size:13px;color:var(--orange)}
.post .cat em{color:var(--muted);font-size:11px;margin-right:6px}
.post .title{top:38px;width:100%;text-align:center;font-size:37px;font-weight:700}
.post .meta{top:106px;left:70px;font-size:13px;color:#666}
.post .likes{top:106px;left:484px;font-size:13px;color:var(--orange);display:flex;gap:5px;align-items:center}
.post .likes b{width:8px;height:8px;background:var(--orange);display:inline-block;border-radius:2px}
.post .media{top:159px;left:0;width:674px;height:423px}
.post .tag{top:179px;left:15px;width:215px;height:40px;background:var(--orange);color:#fff;font-size:16px;display:flex;align-items:center;justify-content:center}
.play{width:56px;height:56px;border-radius:50%;background:rgba(0,0,0,.55);left:309px;top:342px}
.arrow{width:36px;height:36px;border-radius:50%;background:#fff;border:1px solid #ccc;top:564px}
.post .sub{top:612px;left:0;font-size:22px;font-weight:700;color:var(--orange)}
.post .body{top:662px;left:0;width:674px;font-size:15px;line-height:31px;color:var(--text)}
.post .comment{top:784px;left:0;width:582px;height:52px;box-shadow:0 1px 8px rgba(0,0,0,.15);font-style:italic;font-size:14px;color:#666;padding:17px 18px}
.post .share{top:801px;left:644px;font-size:14px;color:#666;display:flex;align-items:center;gap:7px}
.about{left:807px;top:746px;width:303px;height:484px;background:linear-gradient(180deg,#5d7fb8 0%,#b9a7c6 40%,#c85a55 62%,#c43b2a 100%)}
.about .panel{left:0;top:341px;width:303px;height:143px;background:rgba(228,66,36,.85);color:#fff;text-align:center}
.side-box{left:809px;width:300px;border:2px solid #cfcfcf}
.side-title{font-size:25px;font-weight:700;color:#222}
.cat-item{left:28px;font-size:16px;color:#555;display:flex;align-items:center;gap:12px}
.blog-img{left:26px;width:124px;height:103px}
.blog-txt{left:172px;font-size:13px;font-weight:700;line-height:18px;color:#111}
.blog-txt span{display:block;font-size:9px;color:var(--orange);font-weight:400;margin-top:4px}
.follow{left:807px;top:2727px;width:303px;height:74px;background:#eeeeee}
.fcirc{width:34px;height:34px;border-radius:50%;border:1px solid #777;top:20px}
.pop-title{left:90px;top:2909px;font-size:28px;font-weight:700}
.pop-rule{left:75px;top:2971px;width:1050px;height:1px;background:#ccc}
.card{top:3015px;width:245px;height:302px;background:#f7f7f7}
.card .img{left:0;top:0;width:245px;height:168px}
.card .tag{left:16px;top:18px;padding:4px 7px;background:var(--orange);color:#fff;font-size:11px}
.card .ct{left:22px;top:190px;font-size:17px;line-height:27px;color:#111}
.card .cm{left:22px;top:260px;font-size:13px;color:#333}
.card .cm span{color:var(--orange);font-size:11px}
.footer{left:0;top:3406px;width:1200px;height:262px;background:var(--footer);color:#fff}
.scirc{top:46px;width:40px;height:40px;border-radius:50%;background:var(--orange)}
.ftext{font-size:13px;text-align:center}
</style>
</head>
<body>
<div class="abs topline"></div>
<div class="abs logo"><i></i>VELDAX</div>
<div class="abs nav active" style="left:468px">Home</div>
<div class="abs nav" style="left:548px">Categories</div>
<div class="abs nav" style="left:663px">Services</div>
<div class="abs nav" style="left:760px">Blog</div>
<div class="abs nav" style="left:827px">Contact Us</div>
<div class="abs login">Login</div>

<div class="abs hero" role="img" aria-label="Blurred warehouse shelving with stacked boxes"></div>
<div class="abs hero-title">VELDAX PORTAL</div>
<div class="abs hero-sub">Lorem ipsum dolor sit amet, consectetur adipiscing elit,<br>sed do eiusmod tempor incididunt ut labore et dolore magna aliqua</div>
<div class="abs hero-btn">GET MORE INFO</div>
<div class="abs dot on" style="left:554px"></div>
<div class="abs dot" style="left:580px"></div>
<div class="abs dot" style="left:606px"></div>
<div class="abs dot" style="left:633px"></div>

<article class="abs post" style="top:746px;height:840px">
  <div class="abs cat"><em>in</em>VELDAX-NEWS</div>
  <h2 class="abs title">Lorem ipsum dolor sit amet</h2>
  <div class="abs meta">&#9636; | May 15, 2018 &nbsp;- &nbsp;&#9679; | 3 Comments</div>
  <div class="abs likes">&#9825; 106 | <b></b><b></b><b></b><b></b></div>
  <div class="abs media" role="img" aria-label="Container yard with stacked shipping containers and a forklift" style="background:linear-gradient(180deg,#3a5f9e 0%,#6c7ea0 40%,#8a4b55 60%,#9a9a96 100%)"></div>
  <div class="abs tag">VELDAX-NEWS</div>
  <svg class="abs play" viewBox="0 0 56 56"><path d="M22 17 L39 28 L22 39Z" fill="#fff"/></svg>
  <svg class="abs arrow" style="left:300px" viewBox="0 0 36 36"><path d="M20 12 L14 18 L20 24" stroke="#333" stroke-width="2" fill="none"/></svg>
  <svg class="abs arrow" style="left:338px" viewBox="0 0 36 36"><path d="M16 12 L22 18 L16 24" stroke="#333" stroke-width="2" fill="none"/></svg>
  <h3 class="abs sub">Sed ut perspiciatis unde omnis iste natus error sit</h3>
  <p class="abs body">Lorem ipsum dolor sit amet, consectetur adipiscing elit, sed do eiusmod tempor incididunt ut labore et dolore magna aliqua. Ut enim ad minim veniam, quis nostrud exercitation ullamco laboris nisi ut aliquip ex ea commodo consequat. Duis aute irure dolor in reprehenderit in voluptate velit</p>
  <div class="abs comment">Comment</div>
  <div class="abs share"><svg width="13" height="13" viewBox="0 0 13 13"><circle cx="10" cy="2.5" r="2.2" fill="#444"/><circle cx="2.5" cy="6.5" r="2.2" fill="#444"/><circle cx="10" cy="10.5" r="2.2" fill="#444"/><path d="M10 2.5 L2.5 6.5 L10 10.5" stroke="#444" stroke-width="1.3" fill="none"/></svg>5</div>
</article>

<article class="abs post" style="top:1675px;height:840px">
  <div class="abs cat"><em>in</em>VELDAX-NEWS</div>
  <h2 class="abs title">Lorem ipsum dolor sit amet</h2>
  <div class="abs meta">&#9636; | May 15, 2018 &nbsp;- &nbsp;&#9679; | 3 Comments</div>
  <div class="abs likes">&#9825; 106 | <b></b><b></b><b></b><b></b></div>
  <div class="abs media" role="img" aria-label="Container stacks at dusk with a forklift lifting a container" style="background:linear-gradient(180deg,#3d63b8 0%,#8b7fc0 35%,#c98aa8 50%,#5a4b6a 75%,#2e3550 100%)"></div>
  <div class="abs tag">VELDAX-NEWS</div>
  <svg class="abs play" viewBox="0 0 56 56"><path d="M22 17 L39 28 L22 39Z" fill="#fff"/></svg>
  <svg class="abs arrow" style="left:300px" viewBox="0 0 36 36"><path d="M20 12 L14 18 L20 24" stroke="#333" stroke-width="2" fill="none"/></svg>
  <svg class="abs arrow" style="left:338px" viewBox="0 0 36 36"><path d="M16 12 L22 18 L16 24" stroke="#333" stroke-width="2" fill="none"/></svg>
  <h3 class="abs sub">Sed ut perspiciatis unde omnis iste natus error sit</h3>
  <p class="abs body">Lorem ipsum dolor sit amet, consectetur adipiscing elit, sed do eiusmod tempor incididunt ut labore et dolore magna aliqua. Ut enim ad minim veniam, quis nostrud exercitation ullamco laboris nisi ut aliquip ex ea commodo consequat. Duis aute irure dolor in reprehenderit in voluptate velit</p>
  <div class="abs comment">Comment</div>
  <div class="abs share"><svg width="13" height="13" viewBox="0 0 13 13"><circle cx="10" cy="2.5" r="2.2" fill="#444"/><circle cx="2.5" cy="6.5" r="2.2" fill="#444"/><circle cx="10" cy="10.5" r="2.2" fill="#444"/><path d="M10 2.5 L2.5 6.5 L10 10.5" stroke="#444" stroke-width="1.3" fill="none"/></svg>5</div>
</article>

<aside class="abs about" role="img" aria-label="Container port with cranes and a red shipping container">
  <svg class="abs" style="left:5px;top:154px" width="36" height="36" viewBox="0 0 36 36"><circle cx="18" cy="18" r="17" fill="rgba(255,255,255,.85)"/><path d="M20 12 L14 18 L20 24" stroke="#333" stroke-width="2" fill="none"/></svg>
  <svg class="abs" style="left:261px;top:154px" width="36" height="36" viewBox="0 0 36 36"><circle cx="18" cy="18" r="17" fill="rgba(255,255,255,.85)"/><path d="M16 12 L22 18 L16 24" stroke="#333" stroke-width="2" fill="none"/></svg>
  <div class="abs panel">
    <div style="margin-top:24px;font-size:20px">ABOUT US</div>
    <div style="margin-top:8px;font-size:14px;line-height:22px">Lorem ipsum dolor sit amet, consectetur<br>adipiscing elit, sed do eiu</div>
    <div style="margin-top:8px;font-size:11px">May 14, 2019</div>
  </div>
</aside>

<section class="abs side-box" style="top:1301px;height:695px">
  <h4 class="abs side-title" style="left:28px;top:34px">CATEGORIES</h4>
  <div class="abs cat-item" style="top:97px"><svg width="16" height="16" viewBox="0 0 16 16"><circle cx="8" cy="8" r="8" fill="#ef4a24"/><path d="M4.5 8.2 L7 10.6 L11.5 5.6" stroke="#fff" stroke-width="2" fill="none"/></svg>LOREM IPSUM DOLOR</div>
  <div class="abs cat-item" style="top:142px"><svg width="16" height="16" viewBox="0 0 16 16"><circle cx="8" cy="8" r="8" fill="#ef4a24"/><path d="M4.5 8.2 L7 10.6 L11.5 5.6" stroke="#fff" stroke-width="2" fill="none"/></svg>LOREM IPSUM DOLOR</div>
  <div class="abs cat-item" style="top:187px"><svg width="16" height="16" viewBox="0 0 16 16"><circle cx="8" cy="8" r="8" fill="#ef4a24"/><path d="M4.5 8.2 L7 10.6 L11.5 5.6" stroke="#fff" stroke-width="2" fill="none"/></svg>LOREM IPSUM DOLOR</div>
  <div class="abs cat-item" style="top:232px"><svg width="16" height="16" viewBox="0 0 16 16"><circle cx="8" cy="8" r="8" fill="#ef4a24"/><path d="M4.5 8.2 L7 10.6 L11.5 5.6" stroke="#fff" stroke-width="2" fill="none"/></svg>LOREM IPSUM DOLOR</div>
  <div class="abs cat-item" style="top:277px"><svg width="16" height="16" viewBox="0 0 16 16"><circle cx="8" cy="8" r="8" fill="#ef4a24"/><path d="M4.5 8.2 L7 10.6 L11.5 5.6" stroke="#fff" stroke-width="2" fill="none"/></svg>LOREM IPSUM DOLOR</div>
  <div class="abs cat-item" style="top:322px"><svg width="16" height="16" viewBox="0 0 16 16"><circle cx="8" cy="8" r="8" fill="#ef4a24"/><path d="M4.5 8.2 L7 10.6 L11.5 5.6" stroke="#fff" stroke-width="2" fill="none"/></svg>LOREM IPSUM DOLOR</div>
  <div class="abs cat-item" style="top:367px"><svg width="16" height="16" viewBox="0 0 16 16"><circle cx="8" cy="8" r="8" fill="#ef4a24"/><path d="M4.5 8.2 L7 10.6 L11.5 5.6" stroke="#fff" stroke-width="2" fill="none"/></svg>LOREM IPSUM DOLOR</div>
  <div class="abs cat-item" style="top:412px"><svg width="16" height="16" viewBox="0 0 16 16"><circle cx="8" cy="8" r="8" fill="#ef4a24"/><path d="M4.5 8.2 L7 10.6 L11.5 5.6" stroke="#fff" stroke-width="2" fill="none"/></svg>LOREM IPSUM DOLOR</div>
  <div class="abs cat-item" style="top:457px"><svg width="16" height="16" viewBox="0 0 16 16"><circle cx="8" cy="8" r="8" fill="#ef4a24"/><path d="M4.5 8.2 L7 10.6 L11.5 5.6" stroke="#fff" stroke-width="2" fill="none"/></svg>LOREM IPSUM DOLOR</div>
  <div class="abs cat-item" style="top:502px"><svg width="16" height="16" viewBox="0 0 16 16"><circle cx="8" cy="8" r="8" fill="#ef4a24"/><path d="M4.5 8.2 L7 10.6 L11.5 5.6" stroke="#fff" stroke-width="2" fill="none"/></svg>LOREM IPSUM DOLOR</div>
  <div class="abs cat-item" style="top:547px"><svg width="16" height="16" viewBox="0 0 16 16"><circle cx="8" cy="8" r="8" fill="#ef4a24"/><path d="M4.5 8.2 L7 10.6 L11.5 5.6" stroke="#fff" stroke-width="2" fill="none"/></svg>LOREM IPSUM DOLOR</div>
  <div class="abs cat-item" style="top:592px"><svg width="16" height="16" viewBox="0 0 16 16"><circle cx="8" cy="8" r="8" fill="#ef4a24"/><path d="M4.5 8.2 L7 10.6 L11.5 5.6" stroke="#fff" stroke-width="2" fill="none"/></svg>LOREM IPSUM DOLOR</div>
  <div class="abs cat-item" style="top:637px"><svg width="16" height="16" viewBox="0 0 16 16"><circle cx="8" cy="8" r="8" fill="#ef4a24"/><path d="M4.5 8.2 L7 10.6 L11.5 5.6" stroke="#fff" stroke-width="2" fill="none"/></svg>LOREM IPSUM DOLOR</div>
</section>

<section class="abs side-box" style="top:2067px;height:599px">
  <h4 class="abs side-title" style="left:30px;top:36px">LATEST BLOG</h4>
  <div class="abs blog-img" style="top:92px;background:linear-gradient(135deg,#2b5fa8,#b98a5c)" role="img" aria-label="Parcel on a conveyor"></div>
  <div class="abs blog-txt" style="top:122px">QUIS AUTEM VEL<br>EUM IURE R<span>MAY 15, 2019</span></div>
  <div class="abs blog-img" style="top:209px;background:linear-gradient(135deg,#3c4f8c,#8f7f6a)" role="img" aria-label="Warehouse interior with shelving"></div>
  <div class="abs blog-txt" style="top:239px">QUIS AUTEM VEL<br>EUM IURE R<span>MAY 15, 2019</span></div>
  <div class="abs blog-img" style="top:336px;background:linear-gradient(135deg,#3e6fa8,#b78556)" role="img" aria-label="Cardboard boxes on a blue surface"></div>
  <div class="abs blog-txt" style="top:366px">QUIS AUTEM VEL<br>EUM IURE R<span>MAY 15, 2019</span></div>
  <div class="abs blog-img" style="top:471px;background:linear-gradient(135deg,#3a6aa0,#b2a84a)" role="img" aria-label="Warehouse worker in a safety vest"></div>
  <div class="abs blog-txt" style="top:501px">QUIS AUTEM VEL<br>EUM IURE R<span>MAY 15, 2019</span></div>
  <div class="abs" style="left:261px;top:576px;font-size:14px;color:#888;letter-spacing:1px">&bull;&bull;&bull;</div>
</section>

<div class="abs follow">
  <div class="abs" style="left:24px;top:28px;font-size:14px;font-weight:700;color:#444">FOLLOW US:</div>
  <div class="abs fcirc" style="left:124px"></div>
  <div class="abs fcirc" style="left:167px"></div>
  <div class="abs fcirc" style="left:211px"></div>
  <svg class="abs fcirc" style="left:254px" viewBox="0 0 34 34"><path d="M17 23 L11 17 A3.5 3.5 0 0 1 17 12.5 A3.5 3.5 0 0 1 23 17Z" fill="none" stroke="#555" stroke-width="1.4"/></svg>
</div>

<h2 class="abs pop-title">Most Popular</h2>
<div class="abs pop-rule"></div>
<svg class="abs" style="left:28px;top:3154px" width="18" height="22" viewBox="0 0 18 22"><path d="M13 3 L5 11 L13 19" stroke="#222" stroke-width="2.5" fill="none"/></svg>
<svg class="abs" style="left:1154px;top:3154px" width="18" height="22" viewBox="0 0 18 22"><path d="M5 3 L13 11 L5 19" stroke="#222" stroke-width="2.5" fill="none"/></svg>

<div class="abs card" style="left:77px">
  <div class="abs img" role="img" aria-label="Bright warehouse aisle" style="background:linear-gradient(180deg,#8a8f99,#c9c9cc)"></div>
  <div class="abs tag">Veldax-News</div>
  <div class="abs ct">At vero eos et<br>accusamus et iusto</div>
  <div class="abs cm"><span>Veldax-News</span> &nbsp;/ &nbsp;03.01.2018</div>
</div>
<div class="abs card" style="left:344px">
  <div class="abs img" role="img" aria-label="Aerial view of a container ship at sea" style="background:linear-gradient(135deg,#1d7fa8,#c45a3e 55%,#1d6f95)"></div>
  <div class="abs tag">Veldax-News</div>
  <div class="abs ct">At vero eos et<br>accusamus et iusto</div>
  <div class="abs cm"><span>Veldax-News</span> &nbsp;/ &nbsp;03.01.2018</div>
</div>
<div class="abs card" style="left:612px">
  <div class="abs img" role="img" aria-label="Tall warehouse racking with pallets" style="background:linear-gradient(90deg,#4a5f8c,#a07a5a 50%,#4a5f8c)"></div>
  <div class="abs tag">Veldax-News</div>
  <div class="abs ct">At vero eos et<br>accusamus et iusto</div>
  <div class="abs cm"><span>Veldax-News</span> &nbsp;/ &nbsp;03.01.2018</div>
</div>
<div class="abs card" style="left:880px">
  <div class="abs img" role="img" aria-label="Forklift in a warehouse aisle" style="background:linear-gradient(90deg,#7a8596,#b9b2a0 60%,#c9a83a)"></div>
  <div class="abs tag">Veldax-News</div>
  <div class="abs ct">At vero eos et<br>accusamus et iusto</div>
  <div class="abs cm"><span>Veldax-News</span> &nbsp;/ &nbsp;03.01.2018</div>
</div>

<footer class="abs footer">
  <div class="abs scirc" style="left:473px"></div>
  <div class="abs scirc" style="left:527px"></div>
  <div class="abs scirc" style="left:579px"></div>
  <div class="abs scirc" style="left:633px"></div>
  <svg class="abs scirc" style="left:686px" viewBox="0 0 40 40"><path d="M20 28 L12 20 A4.5 4.5 0 0 1 20 14 A4.5 4.5 0 0 1 28 20Z" fill="#fff"/></svg>
  <div class="abs ftext" style="left:0;width:1200px;top:126px;font-size:14px">ADDRESS</div>
  <div class="abs ftext" style="left:233px;width:200px;top:161px">INFO@VELDAX-MAIL.COM</div>
  <div class="abs ftext" style="left:460px;width:280px;top:161px;line-height:23px">48 HARBOR LINE RD, UNIT 9,<br>PORTVALE, OR 00000</div>
  <div class="abs ftext" style="left:800px;width:160px;top:161px">555.010.2200</div>
  <div class="abs ftext" style="left:0;width:1200px;top:232px;font-size:12px">&copy; 2019 The Cmpany name - All registered</div>
</footer>
</body>
</html>
```